Summit Grading a Builders LLC business card

My current business card is very plain. it has my logo and contact information. I woud like something that stands out from the rest. please take a look at my website to see about my company.

Compayt Name - Summit Grading And Builders
Owner - Martin Kowalczyk
Business Address
Business Website - www.summitgradingandbuilders.example
Email - Summitgradingandbuilders@mailbox.example
Phone - 555-214-7390
Fax - 555-806-3127

Target Market(s)

Everyone age tang is 18 - 85

Industry/Entity Type

Business

Contact Information for Business Card

Nice and professional all in one.

Font styles to use
Serif
Other font styles liked:
• Up to you

Requirements
Must have
• All contact info. The design is up to you.
Nice to have
• All the contact info the design is up to you
Should not have
• I don't have any

```html
<!DOCTYPE html>
<html lang="en">
<head>
<meta charset="utf-8">
<title>Summit Grading And Builders – Business Card</title>
<link rel="stylesheet" href="https://fonts.googleapis.com/css2?family=Tinos:wght@400;700&display=swap">
<style>
  :root {
    --stage: #2f2926;
    --paper: #ffffff;
    --ink: #3b3b3b;
    --grey: #7d7d80;
    --band: #8e8e91;
    --orange: #f07f1d;
    --rule: #6a6a6a;
    --faint: #efefef;
  }
  * { margin: 0; padding: 0; box-sizing: border-box; }
  html, body { width: 1200px; height: 780px; overflow: hidden; }
  body {
    background: var(--stage);
    font-family: "Tinos", "Times New Roman", serif;
    color: var(--ink);
    position: relative;
  }
  .card {
    position: absolute;
    top: 235px;
    width: 540px;
    height: 309px;
    background: var(--paper);
    overflow: hidden;
  }
  .card--front { left: 40px; }
  .card--back { left: 620px; }

  /* brand lockup */
  .brand {
    position: absolute;
    display: flex;
    align-items: center;
    gap: 12px;
  }
  .brand__dot {
    width: 34px; height: 34px;
    border-radius: 50%;
    background: var(--orange);
    flex: none;
  }
  .brand__name {
    color: var(--grey);
    font-weight: 700;
    text-transform: uppercase;
    letter-spacing: 1.5px;
    line-height: 1.05;
  }
  .card--front .brand { left: 34px; top: 44px; }
  .card--front .brand__name { font-size: 21px; }
  .card--back .brand { left: 78px; top: 104px; }
  .card--back .brand__dot { width: 48px; height: 48px; }
  .card--back .brand__name { font-size: 30px; }

  /* faint decoration */
  .front__mark {
    position: absolute;
    left: 250px; top: 20px;
    width: 210px; height: 210px;
    border-radius: 50%;
    background: var(--faint);
  }

  .person {
    position: absolute;
    right: 36px; top: 58px;
    text-align: right;
  }
  .person__name { font-size: 20px; font-weight: 700; color: var(--ink); }
  .person__role { font-size: 15px; color: var(--orange); }

  .front__rule {
    position: absolute;
    left: 34px; right: 36px; top: 108px;
    border-top: 1.5px solid var(--rule);
  }

  .contact {
    position: absolute;
    left: 34px; top: 126px;
    font-size: 15px;
    line-height: 1.2;
  }
  .contact__address { margin-bottom: 6px; padding-bottom: 6px; border-bottom: 1px solid var(--rule); }
  .contact__row { display: flex; align-items: center; gap: 8px; margin-bottom: 3px; }
  .contact__icon {
    width: 16px; height: 16px;
    background: var(--orange);
    border-radius: 2px;
    display: flex; align-items: center; justify-content: center;
    flex: none;
  }
  .contact__web { margin-top: 16px; font-size: 16px; }

  .badges {
    position: absolute;
    right: 36px; bottom: 40px;
    display: flex;
    align-items: flex-end;
    gap: 16px;
  }
  .badge { background: var(--grey); }
  .badge--seal { width: 58px; height: 58px; border-radius: 50%; border: 4px solid #d6d6d6; }
  .badge--ribbon { width: 62px; height: 50px; background: var(--orange); border-radius: 4px; }
  .badge--shield { width: 54px; height: 58px; border-radius: 8px 8px 14px 14px; border: 3px solid #d6d6d6; }

  .services {
    position: absolute;
    left: 0; right: 0; bottom: 30px;
    height: 28px;
    background: var(--band);
    color: #fff;
    font-size: 15px;
    display: flex; align-items: center; justify-content: center;
    letter-spacing: 0.2px;
  }
</style>
</head>
<body>

<section class="card card--front" aria-label="Business card front">
  <div class="front__mark" aria-hidden="true"></div>
  <div class="brand">
    <span class="brand__dot"></span>
    <span class="brand__name">Summit Grading<br>And Builders</span>
  </div>
  <div class="person">
    <div class="person__name">Martin Kowalczyk</div>
    <div class="person__role">Owner</div>
  </div>
  <div class="front__rule"></div>
  <div class="contact">
    <div class="contact__address">4820 Ridge Avenue,<br>Millbrook, NY, United States</div>
    <div class="contact__row">
      <span class="contact__icon"><svg width="11" height="8" viewBox="0 0 11 8"><rect x="0.5" y="0.5" width="10" height="7" fill="none" stroke="#fff"/><path d="M0.5 0.5 L5.5 4.5 L10.5 0.5" fill="none" stroke="#fff"/></svg></span>
      <span>Summitgradingandbuilders@mailbox.example</span>
    </div>
    <div class="contact__row">
      <span class="contact__icon"><svg width="10" height="10" viewBox="0 0 10 10"><path d="M2 0.5 L4 2.5 L3 4 Q4.5 6 6 7 L7.5 6 L9.5 8 L8 9.5 Q3 9 0.5 2 Z" fill="#fff"/></svg></span>
      <span>555-214-7390</span>
    </div>
    <div class="contact__row">
      <span class="contact__icon"><svg width="11" height="10" viewBox="0 0 11 10"><rect x="2.5" y="0.5" width="6" height="3" fill="none" stroke="#fff"/><rect x="0.5" y="3.5" width="10" height="4" fill="#fff"/><rect x="2.5" y="7" width="6" height="2.5" fill="none" stroke="#fff"/></svg></span>
      <span>555-806-3127</span>
    </div>
    <div class="contact__web">www.summitgradingandbuilders.example</div>
  </div>
  <div class="badges">
    <span class="badge badge--seal" role="img" aria-label="Screened and approved listing badge"></span>
    <span class="badge badge--ribbon" role="img" aria-label="Elite service listing badge"></span>
    <span class="badge badge--shield" role="img" aria-label="Top rated listing badge"></span>
  </div>
</section>

<section class="card card--back" aria-label="Business card back">
  <div class="brand">
    <span class="brand__dot"></span>
    <span class="brand__name">Summit Grading<br>And Builders</span>
  </div>
  <div class="services">Asphalt Paving | Excavation &amp; Grading | Retaining Walls | Snow Removal</div>
</section>

</body>
</html>
```